Tall Maple website Laser Like Lipo and Facial Rejuvenation busines

I need a website for my Laser Like Lipo and Facial Rejuvenation business called Tall Maple. I purchased the domain name. I have a logo and before and after pictures to include along with basic information about the procedure and pricing information. I would like my website to be used by customers to be able to schedule appointments. My logo and before-and-after pictures are attached.

My business is called Tall Maple. It is a laser like Lipo and facial rejuvenation. I've attached my logo and before and after pictures to use on the website.

These treatments are non invasive and people lose 2-10 inches per treatment. My primary audience will be overweight women 30 years of age or older or those with cellulite. I will have some male customers too but mostly women.

As for the web design, I've never had a website before so I really don't have anything specific in mind. I'm open to considering anything. I'm not a girly, girl and I don't like frilly, fancy stuff. I just want something simple but not to either. I love my logo. That is a great fit for my business and personality. I have increased the budget to include coding.

I do not like pastel colors. I do need colors that compliment my logo.

Target Market(s)

Mostly over weight Women or those with cellulite ages 30 and above. Some men.

Industry/Entity Type

Business

Coding

Coded - Design and coding required

Number of Pages Required

3 page

Font styles to use
Serif

Requirements
Must have
• I want my logo and information section on one page, a page for before and after pictures that enlarge when clicked on. I do not want a slide show, and a page for prices. I previously mentioned a section for them to schedule appointments but have decided that I don't want that.
• I do not like pastel colors. I do need colors that compliment my logo.
Should not have
• Not a slide show

```html
<!DOCTYPE html>
<html lang="en">
<head>
<meta charset="utf-8">
<title>Tall Maple</title>
<link rel="stylesheet" href="https://fonts.googleapis.com/css2?family=Open+Sans:wght@300;400;600&display=swap">
<style>
:root{
  --red:#a3161c;
  --red-soft:#c23a4c;
  --ink:#555;
  --muted:#888;
  --line:#e3e3e3;
  --panel:#f4f4f4;
  --admin:#222;
  --footer:#1f1f1f;
  --footer-line:#333;
  --white:#fff;
}
*{box-sizing:border-box;margin:0;padding:0}
html,body{width:745px;height:1200px;overflow:hidden;background:var(--white);font-family:"Open Sans",Arial,sans-serif;color:var(--ink)}
.page{position:relative;width:745px;height:1200px}
.admin-bar{position:absolute;top:0;left:0;width:745px;height:17px;background:var(--admin);color:#ccc;font-size:7px;display:flex;align-items:center;padding:0 8px;gap:12px}
.admin-bar .howdy{margin-left:auto}
.site-header{position:absolute;top:17px;left:0;width:745px;height:58px;background:var(--white)}
.brand{position:absolute;left:80px;top:17px;display:flex;align-items:center;gap:6px;font-size:15px;font-weight:600;color:var(--red)}
.brand .dot{width:8px;height:8px;border-radius:50%;background:var(--red)}
.main-nav{position:absolute;right:80px;top:19px;display:flex;gap:10px;font-size:9px}
.main-nav a{color:var(--red);text-decoration:none;padding:5px 13px}
.main-nav a.active{background:var(--red);color:var(--white)}
.hero{position:absolute;top:75px;left:0;width:745px;height:273px;background:linear-gradient(90deg,#f6c9d3 0%,#fbe3e8 40%,#f1d4c6 62%,#e7b9a4 80%,#f4ede8 100%)}
.hero h1{position:absolute;top:120px;width:100%;text-align:center;font-weight:300;font-size:29px;color:var(--red-soft)}
.about{position:absolute;top:348px;left:0;width:745px;height:160px;background:var(--panel);text-align:center}
.about h2{margin-top:42px;font-weight:400;font-size:13px;color:var(--muted)}
.about p{width:585px;margin:9px auto 0;font-size:7.5px;line-height:12px;color:#999}
.results{position:absolute;top:521px;left:80px;width:585px;display:flex;justify-content:space-between}
.result{width:123px;height:94px;background:#e9e9e9;display:flex;align-items:center;justify-content:space-between;padding:5px}
.result .shot{width:48px;height:84px;background:linear-gradient(180deg,#8f6a55,#c9a58c)}
.divider{position:absolute;top:675px;left:80px;width:585px;height:1px;background:var(--line)}
.plans{position:absolute;top:712px;left:80px;width:585px;display:flex;justify-content:space-between}
.plan{width:174px;height:201px;border:1px solid var(--line);text-align:center}
.plan-head{background:var(--red);color:var(--white);height:50px;padding-top:9px}
.plan-head h3{font-weight:400;font-size:13px}
.plan-head span{font-size:8px}
.price{height:56px;border-bottom:1px solid var(--line);display:flex;justify-content:center;align-items:center;color:var(--red)}
.price sup{font-size:10px;align-self:flex-start;margin-top:12px}
.price b{font-weight:300;font-size:40px;line-height:1}
.price small{font-size:7px;color:var(--muted);margin-left:3px;align-self:flex-end;margin-bottom:12px}
.cta{display:inline-block;margin-top:30px;border:1px solid var(--red);color:var(--red);font-size:9px;padding:5px 14px}
.site-footer{position:absolute;top:992px;left:0;width:745px;height:208px;background:var(--footer);color:#ccc;font-size:7.5px}
.col{position:absolute;top:28px}
.col h4{color:var(--red-soft);font-weight:400;font-size:10px;margin-bottom:8px}
.col li{list-style:none;line-height:19px}
.col p{line-height:13px}
.footer-brand{position:absolute;left:545px;top:32px;text-align:center;width:120px}
.footer-brand .name{font-size:16px;color:#ddd;font-weight:400}
.footer-brand .tag{font-size:5.5px;color:#999;margin-top:3px}
.footer-rule{position:absolute;top:163px;left:80px;width:585px;height:1px;background:var(--footer-line)}
.copyright{position:absolute;top:180px;width:100%;text-align:center;font-size:7.5px;color:#aaa}
</style>
</head>
<body>
<div class="page">
  <div class="admin-bar"><span>Tall Maple</span><span>0</span><span>+ New</span><span>Edit Page</span><span class="howdy">Howdy, admin</span></div>

  <header class="site-header">
    <div class="brand"><span class="dot"></span>Tall Maple</div>
    <nav class="main-nav">
      <a class="active">Home</a><a>Services</a><a>About</a><a>Contact</a>
    </nav>
  </header>

  <section class="hero" role="img" aria-label="Woman holding her bare shoulder against a soft pink background">
    <h1>Welcome to Tall Maple</h1>
  </section>

  <section class="about">
    <h2>About Us</h2>
    <p>Our laser treatments are non invasive and gentle, with clients losing two to ten inches per session. We offer body contouring, cellulite reduction and facial rejuvenation in a calm, private studio. Book a free consultation and meet our friendly team today.</p>
  </section>

  <section class="results">
    <div class="result"><div class="shot" role="img" aria-label="Before treatment photo"></div><svg width="14" height="12" viewBox="0 0 14 12"><path d="M0 4h8V0l6 6-6 6V8H0z" fill="#a3161c"/></svg><div class="shot" role="img" aria-label="After treatment photo"></div></div>
    <div class="result"><div class="shot" role="img" aria-label="Before treatment photo"></div><svg width="14" height="12" viewBox="0 0 14 12"><path d="M0 4h8V0l6 6-6 6V8H0z" fill="#a3161c"/></svg><div class="shot" role="img" aria-label="After treatment photo"></div></div>
    <div class="result"><div class="shot" role="img" aria-label="Before treatment photo"></div><svg width="14" height="12" viewBox="0 0 14 12"><path d="M0 4h8V0l6 6-6 6V8H0z" fill="#a3161c"/></svg><div class="shot" role="img" aria-label="After treatment photo"></div></div>
    <div class="result"><div class="shot" role="img" aria-label="Before treatment photo"></div><svg width="14" height="12" viewBox="0 0 14 12"><path d="M0 4h8V0l6 6-6 6V8H0z" fill="#a3161c"/></svg><div class="shot" role="img" aria-label="After treatment photo"></div></div>
  </section>

  <div class="divider"></div>

  <section class="plans">
    <div class="plan"><div class="plan-head"><h3>Service 1</h3><span>Lorem ipsum</span></div><div class="price"><sup>$</sup><b>49</b><small>/Treatment</small></div><span class="cta">I want this!</span></div>
    <div class="plan"><div class="plan-head"><h3>Service 2</h3><span>Lorem ipsum</span></div><div class="price"><sup>$</sup><b>59</b><small>/Treatment</small></div><span class="cta">I want this!</span></div>
    <div class="plan"><div class="plan-head"><h3>Service 3</h3><span>Lorem ipsum</span></div><div class="price"><sup>$</sup><b>69</b><small>/Treatment</small></div><span class="cta">I want this!</span></div>
  </section>

  <footer class="site-footer">
    <div class="col" style="left:80px"><h4>Navigation</h4><ul><li>Home</li><li>Services</li><li>About</li><li>Contact</li></ul></div>
    <div class="col" style="left:233px"><h4>Address</h4><p>Complete Address Here, 7218, City</p></div>
    <div class="col" style="left:390px"><h4>Contact</h4><p>Phone: 555.014.2290<br>Fax: 555.014.2291<br>Email: info@tallmaple.com</p></div>
    <div class="footer-brand"><div class="name">Tall Maple</div><div class="tag">Laser Lipo and Facial Rejuvenation</div></div>
    <div class="footer-rule"></div>
    <div class="copyright">© 2015 | Tall Maple. All Rights Reserved.</div>
  </footer>
</div>
</body>
</html>
```